Shopguidance.net

I've attached two different logo's which I both like and would like to see different designs with each logo. I'm starting a retail consulting business and blog. You can view the start of my project at shopguidance.net to get an idea of what I'm creating.
Looking for a design that says creative, strategic and community.
Updates
Hello Everyone,
Thank you for the amazing design so far.
What I Like
- double sided designs, front and back
- one side should be white or green. Customers cannot write on or make notes on an all black card
- Simple, cool, creative is best
My business card will only have the following
- Instagram
- Facebook
- Email
- Website
My new Tag line is
Think Smart. Lead Smart. Work Smart.
My title will be:
Tobin Marlowe
Retail Consultant
Please submit 1 or 2 designs with these specifications.
Thank you,
Tobin
Reason: Looking for a few more designs and have now committed the project and it is no longer refundable. Please read brief and follow specific instructions.
Looking for something simple yet creative. Something that may stand out from most cards.
Thank you,
Tobin
Thank you,
Tobin
Target Market(s)
My main target is retail managers and retail businesses that are focused on leadership and people development.
Industry/Entity Type
Retail
Look and feel
Each slider illustrates characteristics of the customer's brand and the style your logo design should communicate.

```html
<!DOCTYPE html>
<html lang="en">
<head>
<meta charset="utf-8">
<title>Shopguidance business card</title>
<link href="https://fonts.googleapis.com/css2?family=Questrial&family=Roboto:wght@400;700&display=swap" rel="stylesheet">
<style>
  :root {
    --page: #e8e8ea;
    --ink-dark: #222222;
    --brand-green: #5cbf3f;
    --brand-green-light: #8fd14f;
    --brand-green-deep: #1fa83a;
    --paper: #ffffff;
    --text-dark: #111111;
  }
  * { margin: 0; padding: 0; box-sizing: border-box; }
  html, body { width: 1200px; height: 600px; overflow: hidden; }
  body {
    background: var(--page);
    position: relative;
    font-family: "Questrial", sans-serif;
  }
  .card {
    position: absolute;
    top: 152px;
    width: 466px;
    height: 278px;
    border-radius: 15px;
    overflow: hidden;
  }
  .card-front { left: 94px; background: var(--ink-dark); }
  .card-back { left: 638px; background: var(--paper); }

  .wordmark {
    position: absolute;
    display: flex;
    align-items: center;
    color: var(--brand-green);
    font-family: "Questrial", sans-serif;
    white-space: nowrap;
  }
  .wordmark .dot {
    border-radius: 50%;
    background: var(--brand-green);
  }
  .card-front .wordmark {
    left: 0; right: 0; top: 112px;
    justify-content: center;
    font-size: 38px;
    gap: 10px;
  }
  .card-front .wordmark .dot { width: 44px; height: 44px; }
  .tagline {
    position: absolute;
    left: 0; right: 0; top: 243px;
    text-align: center;
    color: var(--paper);
    font-size: 13px;
  }

  .card-back .wordmark {
    left: 18px; top: 40px;
    font-size: 29px;
    gap: 7px;
  }
  .card-back .wordmark .dot { width: 34px; height: 34px; }
  .person {
    position: absolute;
    right: 20px; top: 102px;
    text-align: right;
    font-family: "Roboto", sans-serif;
    color: var(--text-dark);
  }
  .person-name { font-size: 18px; font-weight: 700; line-height: 1.1; }
  .person-title { font-size: 13px; line-height: 1.2; }

  .back-band { position: absolute; left: 0; top: 0; }
  .contact-list {
    position: absolute;
    left: 18px; top: 224px;
    list-style: none;
    color: var(--paper);
    font-size: 13px;
    line-height: 17px;
  }
  .contact-list li { display: flex; align-items: center; gap: 6px; }
  .contact-list svg { width: 11px; height: 11px; }
  .social-links {
    position: absolute;
    left: 325px; top: 240px;
    display: flex; gap: 4px;
  }
  .social-links span {
    width: 16px; height: 16px;
    border-radius: 50%;
    background: var(--paper);
  }
</style>
</head>
<body>
  <section class="card card-front" aria-label="Card front">
    <div class="wordmark"><span class="dot"></span><span>Shopguidance</span></div>
    <p class="tagline">Think Smart. Lead Smart. Work Smart</p>
  </section>

  <section class="card card-back" aria-label="Card back">
    <div class="wordmark"><span class="dot"></span><span>Shopguidance</span></div>
    <div class="person">
      <p class="person-name">Tobin Marlowe</p>
      <p class="person-title">Retail Consultant</p>
    </div>
    <svg class="back-band" width="466" height="278" viewBox="0 0 466 278" aria-hidden="true">
      <defs>
        <linearGradient id="bandGreen" x1="0" y1="0" x2="1" y2="0">
          <stop offset="0" stop-color="var(--brand-green-light)"/>
          <stop offset="1" stop-color="var(--brand-green-deep)"/>
        </linearGradient>
      </defs>
      <path d="M0,160 C80,190 150,214 230,205 C320,196 380,150 466,136 L466,278 L0,278 Z" fill="url(#bandGreen)"/>
      <path d="M0,176 C80,204 160,222 240,214 C330,205 390,176 466,168 L466,278 L0,278 Z" fill="var(--ink-dark)"/>
      <circle cx="422" cy="220" r="52" fill="var(--brand-green)"/>
    </svg>
    <ul class="contact-list">
      <li>
        <svg viewBox="0 0 12 12" aria-hidden="true"><rect x="0.5" y="2" width="11" height="8" fill="#fff"/><path d="M0.5,2 L6,6.5 L11.5,2" fill="none" stroke="#222" stroke-width="1"/></svg>
        Tobin@shopguidance.net
      </li>
      <li>
        <svg viewBox="0 0 12 12" aria-hidden="true"><g fill="none" stroke="#fff" stroke-width="1"><circle cx="6" cy="6" r="5"/><ellipse cx="6" cy="6" rx="2.2" ry="5"/><path d="M1,6 H11 M2,3.5 H10 M2,8.5 H10"/></g></svg>
        www.shopguidance.net
      </li>
    </ul>
    <div class="social-links" role="img" aria-label="Social network links">
      <span></span><span></span>
    </div>
  </section>
</body>
</html>
```